Copper Lantern Vapors - Premium labels

Copper Lantern Vapors is a business that has multiple retail locations where we sell e-cigs and liquid for e-cigs. We have our own house line of liquid but we're looking for expand our business with a premium brand of liquid. This label would be for our premium liquid bottles. We'd like to go with a Four Horseman of the Apocalypse theme. So I'm thinking we would have 4 flavors named White, Black, Red, and Pale.

Example label template attached.

Please let me know if you have any questions!

Thanks
(attaching our standard logo as reference)

Industry/Entity Type

Business

Requirements
Must have
• The branding should be for The Last Riders theme. We want this to seem like it's own brand. Should have four different variations of labels - one each for White, Black, Red, and Pale. They can be very similar (or different), no preference at the moment.

```html
<!DOCTYPE html>
<html lang="en">
<head>
<meta charset="utf-8">
<title>Copper Lantern Vapors – The Last Riders Labels</title>
<link rel="stylesheet" href="https://fonts.googleapis.com/css2?family=Orbitron:wght@700;900&display=swap">
<style>
  :root {
    --page-bg: #f1f1f1;
    --ink: #111111;
    --paper: #ffffff;
    --black-art-a: #2e2e2e;
    --black-art-b: #8c8c8c;
    --red-art-a: #2a0505;
    --red-art-b: #c8160f;
    --red-fill: #d21613;
    --red-title: #e0251b;
    --pale-art-a: #5e4038;
    --pale-art-b: #c39d90;
    --pale-fill: #ead3cb;
    --pale-title: #b8978c;
    --pale-ink: #555555;
    --white-art-a: #b9b9b9;
    --white-art-b: #ebebeb;
  }
  * { margin: 0; padding: 0; box-sizing: border-box; }
  html, body { width: 1200px; height: 1039px; overflow: hidden; background: var(--page-bg); }
  .label-row {
    position: absolute; left: 35px; top: 350px;
    display: flex; gap: 30px;
  }
  .label { width: 260px; height: 340px; display: block; box-shadow: 0 2px 8px rgba(0,0,0,.15); }
  .flavour-title {
    font-family: "Orbitron", sans-serif; font-weight: 900; font-size: 38px;
    stroke: var(--ink); stroke-width: 2.5px; paint-order: stroke fill;
  }
  .series-name {
    font-family: "Orbitron", sans-serif; font-weight: 900; font-size: 15px;
    letter-spacing: .5px;
  }
  .brand-name {
    font-family: "Orbitron", sans-serif; font-weight: 700; font-size: 7px;
  }
</style>
</head>
<body>
<main class="label-row">

  <!-- BLACK -->
  <svg class="label label--black" viewBox="0 0 260 340" aria-label="Black flavour label">
    <defs>
      <linearGradient id="art-black" x1="0" y1="0" x2="1" y2="1">
        <stop offset="0" stop-color="var(--black-art-b)"/>
        <stop offset="1" stop-color="var(--black-art-a)"/>
      </linearGradient>
    </defs>
    <rect class="horse-art" width="260" height="340" fill="url(#art-black)" role="img" aria-label="Greyscale painting of charging horses"/>
    <polygon class="corner-panel" points="92,340 260,150 260,340" fill="var(--paper)"/>
    <polygon class="diagonal-band" points="68,340 260,123 260,150 92,340" fill="var(--ink)"/>
    <text class="flavour-title" x="18" y="64" fill="var(--paper)">BLACK</text>
    <text class="series-name" x="170" y="240" text-anchor="middle" dominant-baseline="middle" fill="var(--paper)" transform="rotate(-48.5 170 240)">THE LAST RIDERS</text>
    <circle cx="152" cy="320" r="3" fill="var(--ink)"/>
    <text class="brand-name" x="160" y="322.5" fill="var(--ink)">Copper Lantern Vapors</text>
  </svg>

  <!-- RED -->
  <svg class="label label--red" viewBox="0 0 260 340" aria-label="Red flavour label">
    <defs>
      <linearGradient id="art-red" x1="0" y1="0" x2="1" y2="1">
        <stop offset="0" stop-color="var(--red-art-b)"/>
        <stop offset="1" stop-color="var(--red-art-a)"/>
      </linearGradient>
    </defs>
    <rect class="horse-art" width="260" height="340" fill="url(#art-red)" role="img" aria-label="Red-tinted painting of charging horses"/>
    <polygon class="corner-panel" points="92,340 260,150 260,340" fill="var(--red-fill)"/>
    <polygon class="diagonal-band" points="68,340 260,123 260,150 92,340" fill="var(--red-art-a)"/>
    <text class="flavour-title" x="18" y="64" fill="var(--red-title)">RED</text>
    <text class="series-name" x="170" y="240" text-anchor="middle" dominant-baseline="middle" fill="var(--red-fill)" transform="rotate(-48.5 170 240)">THE LAST RIDERS</text>
    <circle cx="152" cy="320" r="3" fill="var(--ink)"/>
    <text class="brand-name" x="160" y="322.5" fill="var(--ink)">Copper Lantern Vapors</text>
  </svg>

  <!-- PALE -->
  <svg class="label label--pale" viewBox="0 0 260 340" aria-label="Pale flavour label">
    <defs>
      <linearGradient id="art-pale" x1="0" y1="0" x2="1" y2="1">
        <stop offset="0" stop-color="var(--pale-art-b)"/>
        <stop offset="1" stop-color="var(--pale-art-a)"/>
      </linearGradient>
    </defs>
    <rect class="horse-art" width="260" height="340" fill="url(#art-pale)" role="img" aria-label="Sepia-toned painting of charging horses"/>
    <polygon class="corner-panel" points="68,340 260,123 260,340" fill="var(--pale-fill)"/>
    <text class="flavour-title" x="18" y="64" fill="var(--pale-title)">PALE</text>
    <text class="series-name" x="170" y="240" text-anchor="middle" dominant-baseline="middle" fill="var(--pale-ink)" transform="rotate(-48.5 170 240)">THE LAST RIDERS</text>
    <circle cx="152" cy="320" r="3" fill="var(--pale-ink)"/>
    <text class="brand-name" x="160" y="322.5" fill="var(--pale-ink)">Copper Lantern Vapors</text>
  </svg>

  <!-- WHITE -->
  <svg class="label label--white" viewBox="0 0 260 340" aria-label="White flavour label">
    <defs>
      <linearGradient id="art-white" x1="0" y1="0" x2="1" y2="1">
        <stop offset="0" stop-color="var(--white-art-b)"/>
        <stop offset="1" stop-color="var(--white-art-a)"/>
      </linearGradient>
    </defs>
    <rect class="horse-art" width="260" height="340" fill="url(#art-white)" role="img" aria-label="Light silver painting of charging horses"/>
    <polygon class="corner-panel" points="68,340 260,123 260,340" fill="var(--ink)"/>
    <text class="flavour-title" x="18" y="64" fill="var(--paper)">WHITE</text>
    <text class="series-name" x="170" y="240" text-anchor="middle" dominant-baseline="middle" fill="var(--paper)" transform="rotate(-48.5 170 240)">THE LAST RIDERS</text>
    <circle cx="152" cy="320" r="3" fill="var(--paper)"/>
    <text class="brand-name" x="160" y="322.5" fill="var(--paper)">Copper Lantern Vapors</text>
  </svg>

</main>
</body>
</html>
```